Tarrow Building Performance

Id like for my business card to be very bold and professional. Incorporating the business logo, the main services offered, and my contact info. Services are spray foam, insulation, new construction, retrofit, weatherization.

When opening this project sketch harbor was not able to upload my new logo that I picked from another recent sketch harbor project. Does anyone know how i could upload my logo onto the page for design of the business cards?

Target Market(s)

Building owners, contractors

Industry/Entity Type

Building Insulation and performance improvements

Contact Information for Business Card

Owner, Email dean@tarrowbuildingperformance.example Phone number 555-208-6147

Colors
0054AA
0677BA
7BADD7
CADEEF
E8F1F8
F0912C
F2A743
F7CA91
FBE8D2
FDF5EE

Requirements
Must have
• Services- spray foam, cellulose, mineral wool, fiberglass, air sealing, new construction, retrofit, weatherization, energy saving assesments

```html
<!DOCTYPE html>
<html lang="en">
<head>
<meta charset="utf-8">
<title>Tarrow Building Performance – Business Card</title>
<link href="https://fonts.googleapis.com/css2?family=Montserrat:wght@700;800&family=Roboto:wght@400;500&family=Questrial&display=swap" rel="stylesheet">
<style>
  :root {
    --stage: #1b1c1e;
    --navy: #101937;
    --sky: #5bb3e3;
    --orange: #e8730f;
    --white: #ffffff;
  }
  * { box-sizing: border-box; margin: 0; padding: 0; }
  html, body { width: 1200px; height: 900px; overflow: hidden; }
  body { background: var(--stage); position: relative; font-family: "Roboto", Arial, sans-serif; }

  .card {
    position: absolute;
    width: 630px;
    height: 360px;
    background: var(--navy);
    border-radius: 18px;
    overflow: hidden;
    color: var(--white);
  }
  .card--services { left: 60px; top: 55px; }
  .card--contact { left: 510px; top: 485px; }

  .wordmark {
    position: absolute;
    display: flex;
    align-items: center;
    gap: 12px;
  }
  .wordmark__square { width: 22px; height: 22px; background: var(--orange); flex: none; }
  .wordmark__name {
    font-family: "Montserrat", Arial, sans-serif;
    font-weight: 800;
    font-size: 30px;
    line-height: 1.05;
    color: var(--orange);
    letter-spacing: 0.5px;
    text-transform: uppercase;
  }
  .card--services .wordmark { left: 150px; top: 58px; }
  .card--contact .wordmark { left: 175px; top: 48px; }

  .services__title {
    position: absolute;
    left: 0; right: 0; top: 168px;
    text-align: center;
    font-family: "Montserrat", Arial, sans-serif;
    font-weight: 700;
    font-size: 27px;
    color: var(--sky);
    letter-spacing: 0.5px;
  }
  .services__list {
    position: absolute;
    left: 20px; right: 20px; top: 215px;
    font-family: "Questrial", Arial, sans-serif;
    font-size: 21px;
    line-height: 38px;
    text-align: center;
    list-style: none;
  }
  .services__row { white-space: nowrap; }
  .services__dot { color: var(--orange); margin: 0 7px; }

  .owner {
    position: absolute;
    left: 20px; top: 195px;
    width: 215px;
    text-align: right;
  }
  .owner__name {
    font-family: "Montserrat", Arial, sans-serif;
    font-weight: 700;
    font-size: 25px;
    color: var(--sky);
    white-space: nowrap;
  }
  .owner__role { font-size: 18px; margin-top: 2px; }

  .divider {
    position: absolute;
    left: 250px; top: 165px;
    width: 2px; height: 105px;
    background: linear-gradient(var(--navy), var(--orange), var(--navy));
  }

  .contact {
    position: absolute;
    left: 268px; top: 160px;
    list-style: none;
    font-size: 15px;
  }
  .contact__item { display: flex; align-items: center; gap: 10px; height: 36px; white-space: nowrap; }
  .contact__icon { width: 18px; height: 18px; flex: none; }

  .address {
    position: absolute;
    left: 0; right: 0; top: 296px;
    text-align: center;
    font-size: 17px;
  }

  .edge-stripe {
    position: absolute;
    left: 0; right: 0; bottom: 0;
    height: 9px;
    background: linear-gradient(90deg, var(--sky) 0 70%, var(--orange) 70% 100%);
  }
</style>
</head>
<body>

<section class="card card--services" aria-label="Card front – services">
  <div class="wordmark">
    <span class="wordmark__square"></span>
    <span class="wordmark__name">Tarrow Building Performance</span>
  </div>
  <h2 class="services__title">SERVICES</h2>
  <ul class="services__list">
    <li class="services__row"><span class="services__dot">•</span>Spray foam<span class="services__dot">•</span>Cellulose<span class="services__dot">•</span>Mineral wool,<span class="services__dot">•</span>Fiberglass</li>
    <li class="services__row"><span class="services__dot">•</span>Air sealing<span class="services__dot">•</span>New construction<span class="services__dot">•</span>Retrofit<span class="services__dot">•</span>Weatherization</li>
    <li class="services__row"><span class="services__dot">•</span>Energy saving<span class="services__dot">•</span>Assesments</li>
  </ul>
</section>

<section class="card card--contact" aria-label="Card back – contact">
  <div class="wordmark">
    <span class="wordmark__square"></span>
    <span class="wordmark__name">Tarrow Building Performance</span>
  </div>

  <div class="owner">
    <p class="owner__name">Dean Calloway</p>
    <p class="owner__role">Owner</p>
  </div>

  <div class="divider"></div>

  <ul class="contact">
    <li class="contact__item">
      <svg class="contact__icon" viewBox="0 0 24 24"><path fill="#e8730f" d="M6.6 10.8a15 15 0 0 0 6.6 6.6l2.2-2.2c.3-.3.7-.4 1-.2 1.1.4 2.3.6 3.6.6.6 0 1 .4 1 1V20c0 .6-.4 1-1 1A17 17 0 0 1 3 4c0-.6.4-1 1-1h3.5c.6 0 1 .4 1 1 0 1.3.2 2.5.6 3.6.1.3 0 .7-.2 1z"/></svg>
      <span>555-208-6147</span>
    </li>
    <li class="contact__item">
      <svg class="contact__icon" viewBox="0 0 24 24"><rect x="2" y="5" width="20" height="14" rx="1.5" fill="#e8730f"/><path d="M3 6l9 7 9-7" fill="none" stroke="#101937" stroke-width="1.8"/></svg>
      <span>dean@tarrowbuildingperformance.example</span>
    </li>
    <li class="contact__item">
      <svg class="contact__icon" viewBox="0 0 24 24"><circle cx="12" cy="12" r="9.5" fill="none" stroke="#e8730f" stroke-width="2"/><ellipse cx="12" cy="12" rx="4" ry="9.5" fill="none" stroke="#e8730f" stroke-width="1.6"/><path d="M2.5 12h19" stroke="#e8730f" stroke-width="1.6"/></svg>
      <span>www.tarrowbuildingperformance.example</span>
    </li>
  </ul>

  <p class="address">421, Address line goes here 45452, Country name</p>
  <div class="edge-stripe"></div>
</section>

</body>
</html>
```